Postcard Design

Company Name--kinetic grove
48 Alder Row
Brooklyn New York11231
929-550-0184
www.kineticgroves-studio. example
We are a boutique personal fitness company in a exclusive neighnorhood in Brooklyn New York. We specialize in personal training and innovate new fitness classes such as Cross-Training QVM and Tabata.

We want our brand to be high-end but open to all. Laid-back but experts in the field of fitness. Innovative and flexible. Proffessional, friendly and inspiring.

Personal attention for our clients is a must as well as making sure they succeed. 87% of our clients reach their goals.

Colors should be bright but sophisticated with a little aggression but not intimidation.
Updates

Company Name-And contact info has been updated on the brief

I posted a logo. And the colors on the website have changed. If you could incorporate the website color scheme that would be helpful. If for whatever reason the logo is not here I will try to upload again.

Change the contact info: www.kineticgroves-studio.example You tube: Dorrin and the Kinetic Grove Email: Kineticgroves@kineticgroves-studio.example Verbiage changes: 'The only boutique personal fitness studio in Brooklyn. Featuring uniquely proprietary classes QVM, Cross Training and now Tabata." Verbiage Additions Safe for moms, dads and we offer enhanced childcare with certified child care development teachers with our partner studios. Classes start at $15

Please Add : Use this postcard to receive 10% any service

Hi, I could not upload the logo. However they said that our Logo should be uploaded now as I sent it to them manually.

Target Market(s)

30-40 year old women and new moms looking to do cross fit and personal training. Income 80-85K.

Industry/Entity Type

Boutique

Requirements
Must have
• Highlight Tabata and the excellence of the classes.Tag lines- Increase calorie burn by 20%. Increase muscle tone by 25%.Increase metabolism by 25%. Classes only available by appointment. 30mins or 1 hour.
Nice to have
• Attractive and fit young people having fun. Personal training.
Should not have
• Overly sexual fitness models.

```html
<!DOCTYPE html>
<html lang="en">
<head>
<meta charset="utf-8">
<title>Kinetic Grove – Postcard</title>
<link rel="stylesheet" href="https://fonts.googleapis.com/css2?family=Roboto+Condensed:wght@400;700&display=swap">
<style>
  :root {
    --paper: #ffffff;
    --card: #fdeef6;
    --ink: #2b2b2b;
    --ink-soft: #444444;
    --plum: #a3217d;
    --lime: #3aa935;
    --orange: #e8762b;
    --globe: #2d8fd5;
    --rule: #555555;
    --trim: #777777;
  }
  * { margin: 0; padding: 0; box-sizing: border-box; }
  html, body { width: 1200px; height: 939px; overflow: hidden; background: var(--paper); }
  body { font-family: "Roboto Condensed", "Arial Narrow", sans-serif; color: var(--ink); }
  .canvas { position: relative; width: 1200px; height: 939px; background: var(--paper); }
  .trim-marks { position: absolute; inset: 0; }
  .card { position: absolute; left: 31px; top: 31px; width: 1138px; height: 874px; background: var(--card); }
  .pitch { position: absolute; left: 0; width: 596px; text-align: center; white-space: nowrap; }
  .pitch-lead { top: 99px; font-weight: 700; font-size: 33px; line-height: 48px; color: var(--ink); }
  .pitch-promise { top: 205px; font-weight: 700; font-size: 38px; line-height: 60px; color: var(--plum); }
  .pitch-note { top: 337px; font-size: 23px; line-height: 28px; color: var(--ink-soft); }
  .badges { position: absolute; left: 0; top: 360px; }
  .offer-band { position: absolute; left: 3px; top: 526px; width: 588px; height: 51px; background: var(--plum);
    color: #fff; font-weight: 700; font-size: 23px; line-height: 51px; padding-left: 54px; white-space: nowrap; }
  .contacts { position: absolute; left: 51px; top: 617px; list-style: none; }
  .contacts li { display: flex; align-items: center; height: 47px; font-weight: 700; font-size: 25px; color: var(--ink-soft); white-space: nowrap; }
  .contacts li svg { width: 34px; height: 30px; margin-right: 20px; flex: none; }
  .contacts .phone { font-size: 38px; height: 56px; }
  .stamp-box { position: absolute; left: 915px; top: 63px; width: 156px; height: 206px; border: 2px solid var(--rule); }
  .address-line { position: absolute; left: 629px; width: 442px; border-top: 2px solid var(--rule); }
  .line-1 { top: 432px; }
  .line-2 { top: 523px; }
  .line-3 { top: 614px; }
</style>
</head>
<body>
<div class="canvas">
  <svg class="trim-marks" width="1200" height="939" viewBox="0 0 1200 939" aria-hidden="true">
    <g stroke="var(--trim)" stroke-width="1.5">
      <line x1="0" y1="31" x2="18" y2="31"/><line x1="31" y1="0" x2="31" y2="18"/>
      <line x1="1182" y1="31" x2="1200" y2="31"/><line x1="1169" y1="0" x2="1169" y2="18"/>
      <line x1="0" y1="905" x2="18" y2="905"/><line x1="31" y1="921" x2="31" y2="939"/>
      <line x1="1182" y1="905" x2="1200" y2="905"/><line x1="1169" y1="921" x2="1169" y2="939"/>
    </g>
  </svg>

  <section class="card">
    <p class="pitch pitch-lead">Unique, proprietary classes such as<br>QVM, Tabata and personal training.</p>
    <p class="pitch pitch-promise">Local and expert at<br>getting you into shape.</p>
    <p class="pitch pitch-note">Classes only available by appointment.</p>

    <svg class="badges" width="600" height="160" viewBox="0 0 600 160" aria-label="Classes start at $15, 30 mins or 1 hour">
      <g transform="translate(169,72) scale(1.12) translate(-69,-66)">
        <polygon fill="var(--plum)" points="68,4 76,14 88,8 92,21 105,19 104,32 117,35 111,47 122,54 112,63 120,74 108,80 112,93 99,95 98,108 85,106 80,118 69,111 59,120 53,108 40,111 39,98 26,96 30,83 18,77 26,66 17,57 29,50 24,38 37,35 37,22 50,23 54,11 65,16" transform="translate(0,4)"/>
        <text x="69" y="48" fill="#fff" font-size="19" text-anchor="middle">Classes</text>
        <text x="69" y="68" fill="#fff" font-size="19" text-anchor="middle">start at</text>
        <text x="69" y="94" fill="#fff" font-size="24" font-weight="700" text-anchor="middle">$15</text>
      </g>

      <g transform="translate(296,89)">
        <circle r="50" fill="#fff" stroke="var(--lime)" stroke-width="9"/>
        <g fill="var(--lime)"><circle cx="0" cy="-34" r="5"/><circle cx="-34" cy="0" r="5"/><circle cx="34" cy="0" r="5"/></g>
        <polyline points="-22,8 0,-4 22,-24" fill="none" stroke="var(--lime)" stroke-width="6" stroke-linecap="round"/>
        <text y="28" fill="var(--lime)" font-size="18" font-weight="700" text-anchor="middle">30mins</text>
      </g>
      <text x="377" y="102" fill="var(--ink-soft)" font-size="34" font-weight="700" text-anchor="middle">or</text>
      <g transform="translate(459,89)">
        <circle r="50" fill="#fff" stroke="var(--plum)" stroke-width="9"/>
        <g fill="var(--plum)"><circle cx="0" cy="-34" r="5"/><circle cx="-34" cy="0" r="5"/><circle cx="34" cy="0" r="5"/></g>
        <polyline points="-22,8 0,-4 22,-24" fill="none" stroke="var(--plum)" stroke-width="6" stroke-linecap="round"/>
        <text y="28" fill="var(--plum)" font-size="18" font-weight="700" text-anchor="middle">1 hour</text>
      </g>
    </svg>

    <p class="offer-band">Use this postcard to receive 10%Off. Any service!</p>

    <ul class="contacts">
      <li><svg viewBox="0 0 34 30" aria-hidden="true"><rect x="2" y="6" width="30" height="19" fill="var(--plum)"/><polyline points="2,6 17,17 32,6" fill="none" stroke="#fff" stroke-width="2"/></svg>48 Alder Row, Brooklyn New York 11298</li>
      <li><svg viewBox="0 0 34 30" aria-hidden="true"><rect x="9" y="9" width="16" height="20" rx="8" fill="var(--lime)"/><line x1="17" y1="9" x2="17" y2="17" stroke="#fff" stroke-width="2"/><path d="M17 9 C17 3 12 4 10 1" fill="none" stroke="var(--lime)" stroke-width="2"/></svg>kineticgroves@kineticgroves-studio.example</li>
      <li><svg viewBox="0 0 34 30" aria-hidden="true"><circle cx="17" cy="15" r="13" fill="var(--globe)"/><g fill="none" stroke="#fff" stroke-width="1.5"><ellipse cx="17" cy="15" rx="6" ry="13"/><line x1="4" y1="15" x2="30" y2="15"/><line x1="17" y1="2" x2="17" y2="28"/></g></svg>kineticgroves-studio.example</li>
      <li class="phone"><svg viewBox="0 0 34 30" aria-hidden="true"><path d="M3 12 C3 4 31 4 31 12 L31 15 L24 15 L24 11 L10 11 L10 15 L3 15 Z" fill="var(--orange)"/><rect x="8" y="16" width="18" height="10" rx="3" fill="var(--orange)"/><circle cx="17" cy="21" r="3" fill="#fff"/></svg>929-550-0184</li>
    </ul>

    <div class="stamp-box" aria-label="Stamp area"></div>
    <div class="address-line line-1"></div>
    <div class="address-line line-2"></div>
    <div class="address-line line-3"></div>
  </section>
</div>
</body>
</html>
```